Vexo Whitepaper - PDF/JPEG one page 'front cover' design for Vexo 'Whitepaper' document.

Single page front page design (as PDF/JPEG) modelled on MaplyHub example.

Target Market(s)

Venture capitalists

Industry/Entity Type

Crypto

Font styles to use
Sans Serif

Colors
A7469A
B969AE
D3A5CF
EDDBEB
F8F0F9

Requirements
Must have
• Contemporary 'crypto' design. Text should say "Vexo Whitepaper" at top, split onto two lines like the MaplyHub example. And "October 2021
Nice to have
• I like the example from MaplyHUB that I attached.

```html
<!DOCTYPE html>
<html lang="en">
<head>
<meta charset="utf-8">
<title>Vexo Whitepaper – Front Cover</title>
<link rel="stylesheet" href="https://fonts.googleapis.com/css2?family=Lato:wght@400;700;900&display=swap">
<style>
  :root {
    --navy: #020a1f;
    --plum: #2a0f30;
    --plum-soft: #3a1240;
    --pink: #ef2680;
    --white: #ffffff;
    --brand-grey: #c9c9c9;
  }
  * { margin: 0; padding: 0; box-sizing: border-box; }
  html, body {
    width: 1040px;
    height: 1200px;
    overflow: hidden;
    background: var(--navy);
  }
  .cover {
    position: relative;
    width: 1040px;
    height: 1200px;
    overflow: hidden;
    font-family: "Lato", Arial, sans-serif;
    color: var(--white);
  }
  .cover-texture {
    position: absolute;
    inset: 0;
    background:
      radial-gradient(circle at 20% 30%, var(--plum-soft) 0%, transparent 32%),
      radial-gradient(circle at 85% 20%, var(--plum) 0%, transparent 30%),
      radial-gradient(circle at 75% 70%, var(--plum) 0%, transparent 35%),
      radial-gradient(circle at 15% 85%, var(--plum) 0%, transparent 30%),
      var(--navy);
  }
  .brand {
    position: absolute;
    top: 52px;
    right: 80px;
    display: flex;
    align-items: center;
    gap: 14px;
  }
  .brand-dot {
    width: 22px;
    height: 22px;
    border-radius: 50%;
    background: var(--pink);
  }
  .brand-name {
    font-weight: 700;
    font-size: 54px;
    line-height: 1;
    color: var(--brand-grey);
  }
  .title {
    position: absolute;
    top: 118px;
    left: 0;
    width: 100%;
    text-align: center;
    font-weight: 700;
    font-size: 250px;
    line-height: 1;
    letter-spacing: -4px;
    text-shadow: 4px 5px 6px rgba(0, 0, 0, 0.55);
  }
  .subtitle {
    position: absolute;
    top: 395px;
    left: 0;
    width: 100%;
    text-align: center;
    font-weight: 400;
    font-size: 46px;
    letter-spacing: 0.62em;
    padding-left: 0.62em;
  }
  .emblem {
    position: absolute;
    left: 50%;
    top: 770px;
    transform: translate(-50%, -50%);
  }
  .date {
    position: absolute;
    top: 1092px;
    left: 0;
    width: 100%;
    text-align: center;
    font-weight: 400;
    font-size: 36px;
    letter-spacing: 0.55em;
    padding-left: 0.55em;
  }
</style>
</head>
<body>
  <main class="cover">
    <div class="cover-texture" role="img" aria-label="Soft scattered plum bokeh circles on a deep navy background"></div>

    <div class="brand">
      <span class="brand-dot"></span>
      <span class="brand-name">Vexo</span>
    </div>

    <h1 class="title">Vexo</h1>
    <p class="subtitle">WHITEPAPER</p>

    <svg class="emblem" width="160" height="160" viewBox="0 0 160 160" aria-hidden="true">
      <circle cx="80" cy="80" r="66" fill="var(--navy)" stroke="var(--white)" stroke-width="9"/>
      <circle cx="80" cy="80" r="46" fill="var(--pink)"/>
    </svg>

    <p class="date">OCTOBER 2021</p>
  </main>
</body>
</html>
```